Leaf By Frost - Stationery Design Project

Hi everyone,

We need a business card and a stationary set designed for a new corporate video production company based in Sydney, 'Leaf By Frost'.

The name refers to the mythological 'phoenix' so we would like to see designs that are appropriate to both the name and to a creative film company. The key thing is, we need to appear fresh and creative while maintaining professionalism.

We would like to stick with dark colors for the basis of the card. One idea that came up was obsidian/volcanic rock with the logo cracking through to reveal lava or something fire like. This is just one idea that has come up, but we are of course open to others and would love to see what people can come up with. Extensive use of flames/fire imagery is not really what we are after.

Also, cinematic as opposed to corporate is preferable.

**** UPDATE ****
When I hand over the card to a prospective client, I want them to feel like they are receiving an obsidian plate with inscriptions in it (ie the phoenix). Looking for something elemental and rigid to contrast and complement the graceful lines of the logo.

Designs we require:
- Business card
(We would like a business card that makes use of some of the more premium business card printing options, such as foil stamping, embossing/debossing, painted edges, spot UV etc. Doesnt have to use all these things, only what you feel works, but we are looking for a business card that stands out and is memorable and these nice touches have that effect. For an example of what is possible, check out "http://www.glossvantage.example/base/category/business-card-gallery/".)

- Letter head
- With compliments slip
- Display folder

COPMPANY DETAILS:
ABN: 52 804 319 246
Company Address: 7/18-20 Hollin Ave, Kelmore NSW 2094
Name: Rob K. Deverill
Title: Producer
Contact Number: 0417 352 918
email: rob@leafbyfrost.example
website: www.leafbyfrost.example

ABOUT THE PHOENIX:
The phoenix is a musical bird from mythology, known for its long fancy tail and small plume on the top of its head. They are elegant and graceful and symbolize immortality, endurance and strength, believed to live for 5 centuries before they were reborn from their ashes.
Updates

Hi everyone,

We have just updated the design brief to include business contact information, website etc. should anyone require it for their designs.

Thanks

Rob

Target Market(s)

Other creative businesses and marketing firms.

Industry/Entity Type

Printing

Requirements
Must have
• Basic printing requirements:
- CMYK colour space
- 300dpi resolution
- Color bleed/crop marks etc to allow for trimming where necessary
- Source files upon handover
Should not have
• Overuse of fire/flame imagery

```html
<!DOCTYPE html>
<html lang="en">
<head>
<meta charset="utf-8">
<title>Leaf By Frost – Display Folder</title>
<link rel="stylesheet" href="https://fonts.googleapis.com/css2?family=Montserrat:wght@500&display=swap">
<style>
  :root {
    --backdrop: #c8c6c7;
    --obsidian-deep: #080a16;
    --obsidian-mid: #1b1e2c;
    --slate: #454b4f;
    --paper-white: #ffffff;
    --paper-shade: #d6d6d6;
    --name-text: #cfd1d6;
  }
  html, body {
    margin: 0;
    padding: 0;
    width: 1200px;
    height: 1000px;
    overflow: hidden;
    background: var(--backdrop);
  }
  .folder-sheet {
    display: block;
    width: 1200px;
    height: 1000px;
  }
  .brand-name {
    font-family: "Montserrat", sans-serif;
    font-weight: 500;
    font-size: 9px;
    fill: var(--name-text);
  }
</style>
</head>
<body>
<svg class="folder-sheet" viewBox="0 0 1200 1000" xmlns="http://www.w3.org/2000/svg">
  <defs>
    <linearGradient id="cover-base" x1="0" y1="0" x2="1" y2="1">
      <stop offset="0" stop-color="var(--obsidian-mid)"/>
      <stop offset="1" stop-color="var(--slate)"/>
    </linearGradient>
    <linearGradient id="flap-dark" x1="0" y1="0" x2="1" y2="0">
      <stop offset="0" stop-color="var(--obsidian-deep)"/>
      <stop offset="1" stop-color="#2a2e3a"/>
    </linearGradient>
    <linearGradient id="pocket-dark" x1="0" y1="1" x2="1" y2="0">
      <stop offset="0" stop-color="var(--obsidian-deep)"/>
      <stop offset="1" stop-color="#3a3f46"/>
    </linearGradient>
    <linearGradient id="panel-light" x1="0" y1="0" x2="0" y2="1">
      <stop offset="0" stop-color="#f4f4f4"/>
      <stop offset="1" stop-color="var(--paper-shade)"/>
    </linearGradient>
    <linearGradient id="flap-right" x1="0" y1="0" x2="1" y2="0">
      <stop offset="0" stop-color="#c4c4c4"/>
      <stop offset="0.6" stop-color="var(--paper-white)"/>
    </linearGradient>
    <linearGradient id="flap-left" x1="0" y1="0" x2="1" y2="0">
      <stop offset="0.4" stop-color="var(--paper-white)"/>
      <stop offset="1" stop-color="#d4d4d4"/>
    </linearGradient>
    <filter id="soft-shadow" x="-10%" y="-10%" width="130%" height="130%">
      <feDropShadow dx="3" dy="2" stdDeviation="4" flood-color="#000" flood-opacity="0.45"/>
    </filter>
  </defs>

  <!-- Closed folder, front cover -->
  <g class="cover-closed">
    <rect x="76" y="45" width="332" height="436" fill="url(#cover-base)"/>
    <path class="cover-flap" filter="url(#soft-shadow)" fill="url(#flap-dark)"
          d="M76,45 L92,45 C140,48 170,95 200,200 C235,330 262,420 330,458 C362,474 392,478 404,481 L76,481 Z"/>
    <text class="brand-name" x="100" y="446">Leaf By Frost</text>
  </g>

  <!-- Folder opened with front flap lifted -->
  <g class="cover-open">
    <path class="right-flap" fill="url(#flap-right)"
          d="M782,45 L1115,45 C1110,72 1082,80 1060,90 C1010,115 990,190 970,280 C945,400 880,470 800,483 L782,483 Z"/>
    <rect class="inner-panel" x="447" y="45" width="335" height="438" fill="url(#panel-light)"/>
    <path class="pocket" fill="url(#pocket-dark)"
          d="M675,483 L675,330 C700,313 740,310 782,312 L782,483 Z"/>
    <rect class="card-in-pocket" x="677" y="365" width="68" height="45" rx="4" fill="#1c1f2a" stroke="#4a4f58"/>
    <path class="front-flap" filter="url(#soft-shadow)" fill="url(#flap-dark)"
          d="M447,45 L455,47 C520,52 562,92 600,200 C640,320 680,420 758,450 C774,460 780,470 782,483 L447,483 Z"/>
    <text class="brand-name" x="472" y="446">Leaf By Frost</text>
  </g>

  <!-- Fully unfolded inside spread -->
  <g class="spread-inside">
    <path class="left-flap" fill="url(#flap-left)"
          d="M415,503 L380,503 C340,510 310,540 290,610 C260,730 230,830 150,880 C110,900 80,915 78,940 L415,940 Z"/>
    <rect class="centre-panel" x="415" y="503" width="335" height="437" fill="url(#panel-light)"/>
    <path class="right-flap" fill="url(#flap-right)"
          d="M750,503 L1085,503 C1080,530 1050,540 1030,550 C980,575 960,650 940,740 C910,870 850,935 760,940 L750,940 Z"/>
    <path class="pocket" fill="url(#pocket-dark)"
          d="M415,940 C450,830 540,775 650,767 L750,765 L750,940 Z"/>
    <g class="business-card">
      <rect x="578" y="815" width="134" height="72" rx="6" fill="#1a1d28" stroke="#555b64"/>
      <text class="brand-name" x="645" y="855" text-anchor="middle">Leaf By Frost</text>
    </g>
  </g>
</svg>
</body>
</html>
```